Stylish new business card needed!

Hello everyone! I am in need of a new business card design for an alarm company here in Hurricane WV. I have all fonts, color codes and logos provided for you use! We are a young company and like the style of a clean sleek looking business card. Would like it double sided, one side holding the logo and the other with your design!
Target Market(s)
The people that are looking for the newest tech for home automation and security
Industry/Entity Type
Alarm services; Home automation
Contact Information for Business Card
Name of person; position (Sales; Installer); Phone Number (555.419.7362); Employee cell Number; Website (www.GuardedByVelm.example); Employee Email; Double sided
Look and feel
Each slider illustrates characteristics of the customer's brand and the style your logo design should communicate.

```html
<!DOCTYPE html>
<html lang="en">
<head>
<meta charset="utf-8">
<title>VELM Business Card</title>
<link rel="stylesheet" href="https://fonts.googleapis.com/css2?family=Lato:wght@400;700;900&display=swap">
<style>
  :root {
    --page: #1d1d1e;
    --card: #2b2b2c;
    --card-edge: #f59148;
    --orange: #f7934c;
    --grey: #a3a3a3;
    --text: #e6e6e6;
    --muted: #9b9b9b;
    --rule: #555556;
  }
  * { margin: 0; padding: 0; box-sizing: border-box; }
  html, body { width: 1200px; height: 939px; overflow: hidden; }
  body {
    background: var(--page);
    font-family: "Lato", Arial, sans-serif;
    position: relative;
  }
  .card {
    position: absolute;
    left: 320px;
    width: 560px;
    height: 320px;
    background: var(--card);
    border-radius: 18px;
    box-shadow: 2px 3px 0 var(--card-edge);
    overflow: hidden;
  }
  .card--front { top: 120px; }
  .card--back { top: 500px; }

  .wordmark {
    display: flex;
    align-items: center;
    gap: 12px;
    font-weight: 400;
    color: var(--grey);
    letter-spacing: 2px;
    line-height: 1;
  }
  .wordmark__dot {
    border-radius: 50%;
    background: var(--orange);
    flex: none;
  }
  .card--front .wordmark {
    position: absolute;
    left: 50%; top: 50%;
    transform: translate(-50%, -50%);
    font-size: 110px;
  }
  .card--front .wordmark__dot { width: 26px; height: 26px; }

  .card--back .wordmark {
    position: absolute;
    left: 44px; top: 130px;
    font-size: 64px;
    gap: 8px;
  }
  .card--back .wordmark__dot { width: 16px; height: 16px; }

  .divider {
    position: absolute;
    left: 262px; top: 40px;
    width: 1px; height: 240px;
    background: linear-gradient(to bottom, transparent, var(--rule) 20%, var(--rule) 80%, transparent);
  }
  .contact {
    position: absolute;
    left: 290px; top: 58px;
    width: 260px;
  }
  .contact__name {
    color: var(--orange);
    font-weight: 900;
    font-size: 25px;
    letter-spacing: 0.3px;
  }
  .contact__role {
    color: var(--muted);
    font-size: 15px;
    margin: 2px 0 14px;
  }
  .contact__list { list-style: none; }
  .contact__item {
    display: flex;
    align-items: flex-start;
    gap: 10px;
    color: var(--text);
    font-size: 13px;
    line-height: 19px;
    margin-bottom: 3px;
  }
  .contact__icon {
    width: 12px; height: 12px;
    margin-top: 4px;
    flex: none;
    fill: var(--orange);
  }
</style>
</head>
<body>
  <section class="card card--front" aria-label="Card front">
    <div class="wordmark"><span class="wordmark__dot"></span>VELM</div>
  </section>

  <section class="card card--back" aria-label="Card back">
    <div class="wordmark"><span class="wordmark__dot"></span>VELM</div>
    <div class="divider"></div>
    <div class="contact">
      <div class="contact__name">DANIEL REYES</div>
      <div class="contact__role">Sales &amp; Installer</div>
      <ul class="contact__list">
        <li class="contact__item">
          <svg class="contact__icon" viewBox="0 0 12 12"><path d="M6 0a4 4 0 0 0-4 4c0 3 4 8 4 8s4-5 4-8a4 4 0 0 0-4-4zm0 5.6A1.6 1.6 0 1 1 6 2.4a1.6 1.6 0 0 1 0 3.2z"/></svg>
          <span>Address, City, State<br>Country, Zip Code 01235</span>
        </li>
        <li class="contact__item">
          <svg class="contact__icon" viewBox="0 0 12 12"><path d="M2.4 0.5l2 2.2-1 1.4a7 7 0 0 0 4.5 4.5l1.4-1 2.2 2-1.3 1.9C5.6 11.3 0.7 6.4 0.5 1.8z"/></svg>
          <span>555.419.7362</span>
        </li>
        <li class="contact__item">
          <svg class="contact__icon" viewBox="0 0 12 12"><path d="M3 0h6a1 1 0 0 1 1 1v10a1 1 0 0 1-1 1H3a1 1 0 0 1-1-1V1a1 1 0 0 1 1-1zm0.5 1.5v8h5v-8zM6 10.2a0.6 0.6 0 1 0 0 1.2 0.6 0.6 0 0 0 0-1.2z"/></svg>
          <span>555.419.7380</span>
        </li>
        <li class="contact__item">
          <svg class="contact__icon" viewBox="0 0 12 12"><path d="M0 2h12v8H0zm1 1v0.4l5 3.2 5-3.2V3zm0 1.6V9h10V4.6L6 7.8z"/></svg>
          <span>daniel@guardedbyvelm.example</span>
        </li>
        <li class="contact__item">
          <svg class="contact__icon" viewBox="0 0 12 12"><path d="M6 0a6 6 0 1 0 0 12A6 6 0 0 0 6 0zm0 1c.8.7 1.4 2 1.6 3.5H4.4C4.6 3 5.2 1.7 6 1zM1.1 5.5h2.3c0 .4 0 .7.1 1H1.1a5 5 0 0 1 0-1zm3.3 1h3.2c-.2 1.5-.8 2.8-1.6 3.5-.8-.7-1.4-2-1.6-3.5zm4.2 0c0-.3.1-.6.1-1h2.3a5 5 0 0 1 0 1z"/></svg>
          <span>www.GuardedByVelm.example</span>
        </li>
      </ul>
    </div>
  </section>
</body>
</html>
```